Modern business card and stationary for a dental office
World Class Care
Professional
Dr. Gavin Morrow
General Dentist
4836- 92 Street S.E. Edmonton, AB T6K 3R2
drmorrow@pinehollowdental.ca
pinehollowdental.ca
Family Clinic *Cosmetic Dentistry *Implant Dentistry *services provided by a general dentist

```html
<!DOCTYPE html>
<html lang="en">
<head>
<meta charset="utf-8">
<title>Pine Hollow Dental – Business Card</title>
<link href="https://fonts.googleapis.com/css2?family=Open+Sans:wght@400;600&family=Raleway:wght@500&display=swap" rel="stylesheet">
<style>
  :root{
    --bg:#e6e7e9;
    --navy:#1f4f86;
    --navy-deep:#173d6b;
    --sky:#3aa6df;
    --pale:#cfe7f6;
    --white:#ffffff;
    --ink:#1f4f86;
  }
  *{margin:0;padding:0;box-sizing:border-box}
  html,body{width:1200px;height:895px;overflow:hidden;background:var(--bg);font-family:"Open Sans",sans-serif}
  .stage{position:relative;width:1200px;height:895px}
  .card{position:absolute;left:267px;width:665px;height:380px;overflow:hidden;box-shadow:0 6px 18px rgba(0,0,0,.18)}
  .card--front{top:45px;background:var(--white)}
  .card--back{top:470px;background:radial-gradient(ellipse at 40% 30%,#2a64a3 0%,var(--navy) 45%,var(--navy-deep) 100%)}
  .waves{position:absolute;inset:0}
  .brand{position:absolute;top:62px;left:0;width:100%;text-align:center;color:var(--navy);font-family:"Raleway",sans-serif;font-weight:500;font-size:38px;letter-spacing:1px}
  .brand__dot{display:inline-block;width:26px;height:26px;border-radius:50%;background:var(--sky);margin-right:12px;vertical-align:-2px}
  .identity{position:absolute;left:44px;top:248px;color:var(--white)}
  .identity__name{font-weight:600;font-size:17px}
  .identity__role{font-size:13px;margin:2px 0 10px 18px;opacity:.9}
  .identity__addr{font-size:13px;line-height:1.45}
  .contacts{position:absolute;left:378px;top:232px;list-style:none;color:var(--white);font-size:13px}
  .contacts li{display:flex;align-items:center;gap:8px;height:21px}
  .contacts svg{width:14px;height:14px;flex:none}
  .services{position:absolute;left:60px;top:50px;list-style:none;color:var(--white);font-size:19px;line-height:1.45}
  .services li{position:relative;padding-left:24px}
  .services li::before{content:"";position:absolute;left:0;top:9px;width:11px;height:11px;border-radius:50%;background:var(--sky)}
  .web{position:absolute;left:60px;top:222px;color:var(--white);font-size:14px;letter-spacing:.5px}
  .web b{color:var(--sky);font-weight:600}
</style>
</head>
<body>
<main class="stage">
  <section class="card card--front">
    <svg class="waves" viewBox="0 0 665 380" aria-hidden="true">
      <path d="M0 168 C210 128 430 232 665 146 L665 380 L0 380Z" fill="var(--pale)"/>
      <path d="M0 180 C210 140 430 244 665 158 L665 380 L0 380Z" fill="var(--sky)"/>
      <path d="M0 196 C210 156 430 258 665 176 L665 380 L0 380Z" fill="var(--white)"/>
      <path d="M0 204 C210 166 430 266 665 186 L665 380 L0 380Z" fill="var(--navy)"/>
    </svg>
    <div class="brand"><span class="brand__dot"></span>Pine Hollow Dental</div>
    <div class="identity">
      <div class="identity__name">Dr. Gavin Morrow</div>
      <div class="identity__role">General Dentist</div>
      <div class="identity__addr">4836- 92 Street S.E.<br>Edmonton, AB T6K 3R2</div>
    </div>
    <ul class="contacts">
      <li><svg viewBox="0 0 16 16"><path fill="#fff" d="M4 1l2.5 3-1.5 2a9 9 0 0 0 5 5l2-1.5 3 2.5-1.5 2.5C7 15 1 9 1.5 2.5Z"/></svg>780-555-0142</li>
      <li><svg viewBox="0 0 16 16"><rect x="4" y="1" width="8" height="14" rx="1.5" fill="#fff"/><rect x="5.5" y="3" width="5" height="8" fill="var(--navy)"/></svg>780-555-0187</li>
      <li><svg viewBox="0 0 16 16"><circle cx="8" cy="8" r="7" fill="#fff"/></svg>gavinmorrow</li>
      <li><svg viewBox="0 0 16 16"><rect x="1" y="3" width="14" height="10" rx="1" fill="#fff"/><path d="M1.5 4 8 9l6.5-5" stroke="var(--navy)" fill="none" stroke-width="1.3"/></svg>drmorrow@pinehollowdental.ca</li>
      <li><svg viewBox="0 0 16 16"><circle cx="8" cy="8" r="6.5" fill="none" stroke="#fff" stroke-width="1.5"/><path d="M1.5 8h13M8 1.5c-3 3.5-3 9.5 0 13M8 1.5c3 3.5 3 9.5 0 13" stroke="#fff" fill="none" stroke-width="1.2"/></svg>www.pinehollowdental.ca</li>
    </ul>
  </section>

  <section class="card card--back">
    <ul class="services">
      <li>Family Clinic</li>
      <li>Cosmetic Dentistry</li>
      <li>Implant Dentistry</li>
      <li>services provided by a general dentist</li>
    </ul>
    <div class="web">www.<b>pinehollowdental</b>.ca</div>
  </section>
</main>
</body>
</html>
```